Sale PPC Banner Ad Design Update

We need some Plumora PPC Banner Ad's for our sale altered to include product shots in the background. Attached are some examples that we currently use. We want a similar format/look but with the attached product shots used as the background image. Product image is called "VKSLite Level 7"

Have also included our logo file as well.

Industry/Entity Type

Plumora

Font styles to use
Sans Serif

Requirements
Must have
• The must-have sizes (up to 150kb):
• • Banner: 468 x 60
• • Large mobile banner 320 x 100
• • Leaderboard: 728 x 90
• • Square: 250 x 250
• • Small square: 200 x 200
• • Large rectangle: 336 x 280
Nice to have
• The nice-to-have sizes:
• • Vertical rectangle: 240 x 400
• • Mobile leaderboard: 320 x 50
• • Inline rectangle: 300 x 250
• • Skyscraper: 120 x 600
• • Wide skyscraper: 160 x 600
• • Half-page: 300 x 600
• • Large leaderboard: 970 x 90
• • Billboard: 970 x 250
• • Portrait: 300 x 1050

```html
<!DOCTYPE html>
<html lang="en">
<head>
<meta charset="UTF-8">
<title>Plumora Sale Leaderboard</title>
<link rel="stylesheet" href="https://fonts.googleapis.com/css2?family=Raleway:wght@200;300;500&display=swap">
<style>
  :root {
    --brand-strip: #ffffff;
    --brand-ink: #1b1b1b;
    --sale-gold: #dcc67e;
    --cta-white: #f4f1ea;
    --rug-red: #b8362a;
    --rug-yellow: #d9a21f;
    --rug-blue: #2c3f8f;
    --shade: rgba(18, 14, 16, 0.55);
  }
  * { margin: 0; padding: 0; box-sizing: border-box; }
  html, body {
    width: 1200px;
    height: 148px;
    overflow: hidden;
    background: #ffffff;
  }
  .banner {
    position: relative;
    width: 1200px;
    height: 148px;
    overflow: hidden;
    font-family: "Raleway", sans-serif;
  }
  .product-visual {
    position: absolute;
    left: 74px;
    top: 0;
    width: 1126px;
    height: 148px;
    background:
      linear-gradient(90deg, var(--shade) 0%, rgba(10,8,10,0.75) 40%, rgba(10,8,10,0.7) 62%, var(--shade) 100%),
      linear-gradient(120deg, var(--rug-red) 0%, var(--rug-yellow) 22%, var(--rug-blue) 45%, var(--rug-red) 68%, var(--rug-yellow) 85%, var(--rug-blue) 100%);
  }
  .brand-strip {
    position: absolute;
    left: 0;
    top: 0;
    width: 74px;
    height: 148px;
    background: var(--brand-strip);
    display: flex;
    align-items: center;
    justify-content: center;
  }
  .brand-lockup {
    writing-mode: vertical-rl;
    transform: rotate(180deg);
    display: flex;
    flex-direction: column;
    align-items: center;
    color: var(--brand-ink);
    gap: 4px;
  }
  .brand-name {
    font-size: 26px;
    font-weight: 500;
    line-height: 1;
    letter-spacing: 0.5px;
  }
  .brand-tagline {
    font-size: 8px;
    font-weight: 500;
    letter-spacing: 1.5px;
    line-height: 1;
  }
  .sale-title {
    position: absolute;
    left: 421px;
    top: -4px;
    width: 440px;
    text-align: center;
    color: var(--sale-gold);
    font-size: 115px;
    font-weight: 200;
    letter-spacing: 34px;
    padding-left: 34px;
    line-height: 1;
  }
  .cta {
    position: absolute;
    left: 561px;
    top: 106px;
    width: 160px;
    text-align: center;
    color: var(--cta-white);
    font-size: 15px;
    font-weight: 300;
    letter-spacing: 2px;
    padding-left: 2px;
    line-height: 18px;
    text-decoration: none;
  }
</style>
</head>
<body>
  <div class="banner">
    <div class="product-visual" role="img" aria-label="Product photo of two-tone leather loafers on a colourful patterned rug"></div>
    <div class="brand-strip">
      <div class="brand-lockup">
        <span class="brand-name">Plumora</span>
        <span class="brand-tagline">LUXURY SHOES</span>
      </div>
    </div>
    <h1 class="sale-title">SALE</h1>
    <a class="cta" href="#">SHOP NOW</a>
  </div>
</body>
</html>
```